Christmas Banner for frontpage of website

New online scarf store just opened needs a Christmas Banner stating Free Delivery (UK only). Also if it could incorporate guaranteed Christmas delivery if ordered before 18th (might be too wordy though?) I would really like it to bring some colour to the page. The page is currently black and white with a pink accent and is very simple which is why I would like something modern and elegant, simple but with some colour. It is a shopify store I understand the banner size should be 950px by 290px the website is www.velmorrow.co.uk

Target Market(s)

Ladies

Industry/Entity Type

Store

Requirements
Should not have
• Not to look tacky.

```html
<!DOCTYPE html>
<html lang="en">
<head>
<meta charset="UTF-8">
<title>Christmas Free Delivery Banner</title>
<link rel="stylesheet" href="https://fonts.googleapis.com/css2?family=Fira+Sans:wght@700&family=Fira+Sans+Condensed:wght@700&display=swap">
<style>
  :root {
    --canvas: #ffffff;
    --festive-red: #ed1f27;
    --holly-green: #008c45;
    --snow: #ffffff;
    --ornament-tint: rgba(255, 255, 255, 0.32);
  }
  * { margin: 0; padding: 0; box-sizing: border-box; }
  html, body {
    width: 1200px;
    height: 1000px;
    overflow: hidden;
    background: var(--canvas);
  }
  .canvas {
    position: relative;
    width: 1200px;
    height: 1000px;
  }
  .promo-banner {
    position: absolute;
    left: 125px;
    top: 355px;
    width: 950px;
    height: 290px;
    background: var(--festive-red);
    overflow: hidden;
  }
  .bauble-art {
    position: absolute;
    left: 90px;
    top: 0;
    width: 255px;
    height: 270px;
  }
  .sparkle-art {
    position: absolute;
    left: 840px;
    top: 105px;
    width: 50px;
    height: 48px;
  }
  .headline {
    position: absolute;
    left: 304px;
    top: 139px;
    font-family: "Fira Sans", "Arial Narrow", sans-serif;
    font-weight: 700;
    font-size: 78px;
    line-height: 1;
    letter-spacing: 1px;
    color: var(--snow);
    white-space: nowrap;
  }
  .headline-note {
    position: absolute;
    left: 488px;
    top: 209px;
    font-family: "Fira Sans", "Arial Narrow", sans-serif;
    font-weight: 700;
    font-size: 26px;
    line-height: 1;
    letter-spacing: 1.5px;
    color: var(--snow);
    white-space: nowrap;
  }
  .deadline-strip {
    position: absolute;
    left: 390px;
    top: 246px;
    width: 560px;
    height: 44px;
  }
  .deadline-text {
    position: absolute;
    left: 426px;
    top: 257px;
    font-family: "Fira Sans Condensed", "Arial Narrow", sans-serif;
    font-weight: 700;
    font-size: 22.4px;
    line-height: 1;
    color: var(--snow);
    white-space: nowrap;
  }
</style>
</head>
<body>
  <main class="canvas">
    <section class="promo-banner" aria-label="Christmas free delivery banner">
      <svg class="bauble-art" viewBox="0 0 255 270" role="img" aria-label="Decorative white Christmas bauble with swirls, hanging bow and small stars">
        <circle cx="131" cy="197" r="67" fill="var(--ornament-tint)"/>
        <rect x="60" y="50" width="150" height="75" rx="30" fill="var(--ornament-tint)"/>
      </svg>

      <svg class="sparkle-art" viewBox="0 0 50 48" role="img" aria-label="Decorative cluster of small white stars">
        <rect x="0" y="0" width="50" height="48" rx="12" fill="var(--ornament-tint)"/>
      </svg>

      <h1 class="headline">FREE DELIVERY</h1>
      <p class="headline-note">(UK only).</p>

      <svg class="deadline-strip" viewBox="0 0 560 44" aria-hidden="true">
        <polygon points="0,44 26,0 560,0 560,44" fill="var(--holly-green)"/>
      </svg>
      <p class="deadline-text">Guaranteed Christmas delivery if ordered before 18th.</p>
    </section>
  </main>
</body>
</html>
```